A QUIET AMBER PRIMER ON RANKS

subtitle: AN INTRO TO SEARCH ENGINE OPTIMIZATION
background: white
dimensions: 1562x2500

Target Market(s)

Marketing professionals

Industry/Entity Type

Digital Marketing

Font styles to use
Sans Serif

Colors
ffffff
1b1b1b
3176b5

Requirements
Should not have
• Images or graphics

```html
<!DOCTYPE html>
<html lang="en">
<head>
<meta charset="utf-8">
<title>A Quiet Amber Primer on Ranks — SEO Book Cover</title>
<link href="https://fonts.googleapis.com/css2?family=Roboto+Condensed:wght@300&family=Titillium+Web:wght@900&display=swap" rel="stylesheet">
<style>
  :root {
    --backdrop: #e0e2e1;
    --paper: #ffffff;
    --ink: #1b1b1b;
    --ink-black: #000000;
    --accent: #3176b5;
    --mesh: rgba(236, 236, 236, 0.55);
  }
  * { margin: 0; padding: 0; box-sizing: border-box; }
  html, body {
    width: 1200px;
    height: 1200px;
    overflow: hidden;
    background: var(--backdrop);
  }
  .stage {
    position: relative;
    width: 1200px;
    height: 1200px;
  }
  .cover {
    position: absolute;
    left: 296px;
    top: 111px;
    width: 608px;
    height: 979px;
    background: var(--paper);
    overflow: hidden;
  }
  .cover-texture {
    position: absolute;
    inset: 0;
    background:
      radial-gradient(ellipse 300px 300px at 50% 44%, transparent 62%, var(--mesh) 76%, transparent 92%),
      radial-gradient(ellipse 380px 480px at 50% 55%, transparent 60%, rgba(240, 240, 240, 0.45) 80%, transparent 100%),
      var(--paper);
  }
  .kicker {
    position: absolute;
    top: 250px;
    left: 0;
    width: 100%;
    text-align: center;
    font-family: "Roboto Condensed", sans-serif;
    font-weight: 300;
    font-size: 32px;
    line-height: 1.2;
    color: var(--accent);
  }
  .title {
    position: absolute;
    top: 292px;
    left: 0;
    width: 100%;
    text-align: center;
    font-family: "Titillium Web", sans-serif;
    font-weight: 900;
    font-size: 194px;
    line-height: 1;
    letter-spacing: 2px;
    color: var(--ink-black);
  }
  .author {
    position: absolute;
    top: 886px;
    left: 0;
    width: 100%;
    text-align: center;
    font-family: "Roboto Condensed", sans-serif;
    font-weight: 300;
    font-size: 33px;
    line-height: 1.2;
    color: var(--ink);
  }
</style>
</head>
<body>
  <div class="stage">
    <div class="cover">
      <div class="cover-texture" role="img" aria-label="Faint network pattern of connected dots and lines forming a loose ring"></div>
      <p class="kicker">A Quiet Amber Primer on Ranks</p>
      <h1 class="title">SEO</h1>
      <p class="author">Mara Ellison</p>
    </div>
  </div>
</body>
</html>
```